Stationery for a private security company, "Brennock Security Services Ltd."

Needed is a stationery design for a private security company. The designs must show professionalism and that our company mean nothing but business. Watermark of the company logo on the letterhead page is also a must. The final design must represent innovation and professionalism. It would be great if designers could integrate the colours black and silver onto the cards and letterheads..

Thank you

```html
<!DOCTYPE html>
<html lang="en">
<head>
<meta charset="utf-8">
<title>Brennock Security Services Ltd. — Business Card</title>
<link rel="stylesheet" href="https://fonts.googleapis.com/css2?family=Jost:ital,wght@0,400;0,600;1,400;1,600&display=swap">
<style>
  :root {
    --page-bg: #e6e4e0;
    --card-silver: #cac8c4;
    --card-white: #f2f2f2;
    --band-silver: #c6c4c0;
    --watermark: #bab8b4;
    --ink: #1c1c1c;
    --ink-soft: #555555;
    --divider: #6a6a6a;
  }
  * { box-sizing: border-box; margin: 0; padding: 0; }
  html, body { width: 1200px; height: 900px; overflow: hidden; }
  body {
    background: var(--page-bg);
    font-family: "Jost", sans-serif;
    color: var(--ink);
    position: relative;
  }
  .card {
    position: absolute;
    width: 525px;
    height: 300px;
    overflow: hidden;
    box-shadow: 0 6px 18px rgba(0,0,0,0.18);
  }
  /* Back of card */
  .card--back {
    left: 90px; top: 110px;
    background: var(--card-silver);
  }
  .card__watermark {
    position: absolute;
    inset: 0;
    width: 100%;
    height: 100%;
  }
  .brand-name {
    position: absolute;
    left: 0; right: 0;
    text-align: center;
    font-family: "Jost", sans-serif;
    font-weight: 600;
    color: var(--ink);
    line-height: 1.15;
  }
  .card--back .brand-name { top: 112px; font-size: 30px; }
  .brand-name__sub { display: block; font-size: 0.55em; }

  /* Front of card */
  .card--front {
    left: 585px; top: 490px;
    background: var(--card-white);
  }
  .front__band {
    position: absolute;
    left: 0; right: 0;
    top: 128px; height: 140px;
    background: var(--band-silver);
  }
  .card--front .brand-name { top: 40px; font-size: 21px; }
  .holder {
    position: absolute;
    left: 40px; top: 150px;
    width: 140px;
    text-align: right;
  }
  .holder__name { font-size: 17px; font-weight: 600; font-style: italic; }
  .holder__title { font-size: 15px; font-style: italic; color: var(--ink-soft); }
  .divider {
    position: absolute;
    left: 196px; top: 150px;
    width: 2px; height: 102px;
    background: var(--divider);
  }
  .contact {
    position: absolute;
    left: 212px; top: 146px;
    list-style: none;
    font-size: 16px;
    line-height: 20px;
  }
  .contact__item { display: flex; align-items: flex-start; gap: 14px; margin-bottom: 4px; }
  .contact__icon { width: 16px; height: 16px; flex: none; margin-top: 2px; fill: var(--ink); }
</style>
</head>
<body>

<section class="card card--back" aria-label="Business card back">
  <svg class="card__watermark" viewBox="0 0 525 300" role="img" aria-label="Faint brand watermark area">
    <defs>
      <radialGradient id="wm" cx="0.55" cy="0.5" r="0.55">
        <stop offset="0" stop-color="#bebcb8"/>
        <stop offset="1" stop-color="#cac8c4"/>
      </radialGradient>
    </defs>
    <rect width="525" height="300" fill="url(#wm)"/>
  </svg>
  <p class="brand-name">BRENNOCK<span class="brand-name__sub">Security Services Ltd.</span></p>
</section>

<section class="card card--front" aria-label="Business card front">
  <svg class="front__band" viewBox="0 0 525 140" preserveAspectRatio="none" role="img" aria-label="Faint brand watermark area on silver band">
    <defs>
      <linearGradient id="band" x1="0" x2="1">
        <stop offset="0" stop-color="#c3c1bd"/>
        <stop offset="0.5" stop-color="#c8c6c2"/>
        <stop offset="1" stop-color="#c5c3bf"/>
      </linearGradient>
    </defs>
    <rect width="525" height="140" fill="url(#band)"/>
  </svg>
  <p class="brand-name">BRENNOCK<span class="brand-name__sub">Security Services Ltd.</span></p>

  <div class="holder">
    <p class="holder__name">Daniel Hargreave</p>
    <p class="holder__title">President</p>
  </div>
  <div class="divider"></div>

  <ul class="contact">
    <li class="contact__item">
      <svg class="contact__icon" viewBox="0 0 16 16" aria-hidden="true"><path d="M8 0a5.5 5.5 0 0 0-5.5 5.5C2.5 9.6 8 16 8 16s5.5-6.4 5.5-10.5A5.5 5.5 0 0 0 8 0zm0 8a2.5 2.5 0 1 1 0-5 2.5 2.5 0 0 1 0 5z"/></svg>
      <span>000 Larkfield Ave Suite 000<br>Westbrook, CA 90000</span>
    </li>
    <li class="contact__item">
      <svg class="contact__icon" viewBox="0 0 16 16" aria-hidden="true"><path d="M1 5c0-2 3-3 7-3s7 1 7 3v1h-3.5V4.5h-7V6H1zM3 7h10l1 7H2zm5 1.8a2.2 2.2 0 1 0 0 4.4 2.2 2.2 0 0 0 0-4.4z"/></svg>
      <span>000 000 0000</span>
    </li>
    <li class="contact__item">
      <svg class="contact__icon" viewBox="0 0 16 16" aria-hidden="true"><path d="M4 0h8v5H4zM1 6h14v8H1zm3 2v1h8V8zm0 2.5v1h8v-1z"/></svg>
      <span>000 000 0000</span>
    </li>
    <li class="contact__item">
      <svg class="contact__icon" viewBox="0 0 16 16" aria-hidden="true"><path d="M0 3h16v10H0zm1.5 1.2v.3L8 9l6.5-4.5v-.3zM1.5 6.3V12h13V6.3L8 10.8z"/></svg>
      <span>name@company.com.nz</span>
    </li>
  </ul>
</section>

</body>
</html>
```